Sunny Paths and joy Business card

I have a logo, but will like a business card design. Is for a travel agency in Mexico. We focus in family experiences.

I will liek some thing different and unique, from the traditional business card, something to get remmeber for.

Business card information:

Leandro T. Ocampo
leandro@sunnypathsjoy.example

Alameda 482, 3 piso
Col. Tlalpizco
Mexico, D.F. 07320

office: (55) 5000-0142
mobile: (55) 9000-0187

www.sunnypathsjoy.example
@sunnypjoy
blog: sunnypathsandjoy.blogsite.example
facebook: SunnyPathsAndJoy

```html
<!DOCTYPE html>
<html lang="en">
<head>
<meta charset="utf-8">
<title>Sunny Paths and joy – Business Card</title>
<link rel="stylesheet" href="https://fonts.googleapis.com/css2?family=Andika:wght@400;700&family=Open+Sans:wght@400;600&display=swap">
<style>
  :root {
    --page-bg: #ecebe8;
    --card-bg: #ffffff;
    --brand-blue: #1f4d8f;
    --brand-blue-light: #9fcbea;
    --name-blue: #1b6497;
    --text-grey: #4a4a4a;
    --divider: #c9ccd0;
    --illus-sky: #cfe6f6;
    --illus-plane: #3a6fc0;
    --blog-orange: #e8742a;
    --social-blue: #3b5b9a;
  }
  * { box-sizing: border-box; margin: 0; padding: 0; }
  html, body { width: 1200px; height: 511px; overflow: hidden; }
  body {
    background: var(--page-bg);
    font-family: "Open Sans", Arial, sans-serif;
    position: relative;
  }
  .card {
    position: absolute;
    top: 108px;
    width: 515px;
    height: 294px;
    background: var(--card-bg);
    box-shadow: 0 2px 6px rgba(0,0,0,.18);
    overflow: hidden;
  }
  .card--front { left: 59px; }
  .card--back { left: 627px; }

  .logo-art {
    position: absolute;
    border-radius: 46% 54% 40% 60% / 55% 50% 50% 45%;
    background: radial-gradient(ellipse at 55% 55%, var(--illus-plane) 0 38%, var(--illus-sky) 40% 100%);
  }
  .logo-name {
    position: absolute;
    font-family: "Andika", "Comic Sans MS", sans-serif;
    font-weight: 700;
    color: var(--brand-blue);
    text-align: center;
    line-height: 1.05;
  }

  /* Front */
  .card--front .logo-art { left: 98px; top: 60px; width: 138px; height: 84px; }
  .card--front .logo-name { left: 20px; top: 146px; width: 240px; font-size: 26px; }
  .divider {
    position: absolute; left: 282px; top: 100px;
    width: 1px; height: 124px; background: var(--divider);
  }
  .holder-name {
    position: absolute; left: 296px; top: 112px;
    font-family: "Andika", "Comic Sans MS", sans-serif;
    font-weight: 400;
    font-size: 19px; color: var(--name-blue);
  }
  .contact-list {
    position: absolute; left: 295px; top: 152px;
    list-style: none; font-size: 11.5px; color: var(--text-grey);
  }
  .contact-list li { display: flex; align-items: center; height: 16.5px; white-space: nowrap; }
  .contact-list svg { width: 10px; height: 10px; margin-right: 7px; flex: none; }
  .band { position: absolute; left: 0; bottom: 0; width: 515px; height: 70px; }
  .address {
    position: absolute; left: 35px; bottom: 12px;
    font-size: 12.5px; color: #fff; letter-spacing: .2px;
  }

  /* Back */
  .card--back .logo-art { left: 195px; top: 58px; width: 132px; height: 80px; }
  .card--back .logo-name { left: 140px; top: 134px; width: 240px; font-size: 25px; }
  .links {
    position: absolute; left: 140px; top: 208px;
    list-style: none; font-size: 13px; color: var(--text-grey);
  }
  .links li { display: flex; align-items: center; height: 20px; margin-bottom: 18px; white-space: nowrap; }
  .links .mark { width: 20px; height: 20px; border-radius: 3px; margin-right: 8px; flex: none; }
  .links .mark--blog { background: var(--blog-orange); }
  .links .mark--social { background: var(--social-blue); }
  .links li:last-child { margin-left: 48px; }
</style>
</head>
<body>

<section class="card card--front">
  <div class="logo-art" role="img" aria-label="Illustration: cartoon blue airplane with two waving children against a light blue cloud"></div>
  <div class="logo-name">Sunny Paths<br>and joy</div>

  <div class="divider"></div>
  <h1 class="holder-name">Leandro T. Ocampo</h1>
  <ul class="contact-list">
    <li><svg viewBox="0 0 10 10"><circle cx="5" cy="5" r="4.3" fill="none" stroke="#4a4a4a" stroke-width="1.2"/><path d="M3.2 3 L4.2 3 L4.6 4.3 L4 4.8 Q4.8 6 5.8 6.3 L6.3 5.7 L7.3 6.1 L7.2 7 Q5.4 7.3 3.9 5.6 Q2.9 4.2 3.2 3Z" fill="#4a4a4a"/></svg>(55) 5000-0142</li>
    <li><svg viewBox="0 0 10 10"><rect x="2.8" y="0.6" width="4.4" height="8.8" rx="0.8" fill="#4a4a4a"/><rect x="3.6" y="1.8" width="2.8" height="4.4" fill="#fff"/></svg>(55) 9000-0187</li>
    <li><svg viewBox="0 0 10 10"><rect x="0.8" y="2.2" width="8.4" height="5.8" rx="0.8" fill="#4a4a4a"/><path d="M1.2 2.8 L5 5.6 L8.8 2.8" fill="none" stroke="#fff" stroke-width="0.9"/></svg>leandro@sunnypathsjoy.example</li>
    <li><svg viewBox="0 0 10 10"><circle cx="5" cy="5" r="4.3" fill="#4a4a4a"/><path d="M0.8 5 H9.2 M5 0.8 Q2.4 5 5 9.2 M5 0.8 Q7.6 5 5 9.2" fill="none" stroke="#fff" stroke-width="0.7"/></svg>www.sunnypathsjoy.example</li>
  </ul>

  <svg class="band" viewBox="0 0 515 70" preserveAspectRatio="none" aria-hidden="true">
    <path d="M0 8 Q250 -12 515 32 L515 70 L0 70 Z" fill="var(--brand-blue-light)"/>
    <path d="M0 16 Q250 2 515 44 L515 70 L0 70 Z" fill="var(--brand-blue)"/>
  </svg>
  <p class="address">Alameda 482, 3 piso. Col. Tlalpizco Mexico, D.F. 07320</p>
</section>

<section class="card card--back">
  <div class="logo-art" role="img" aria-label="Illustration: cartoon blue airplane with two waving children against a light blue cloud"></div>
  <div class="logo-name">Sunny Paths<br>and joy</div>
  <ul class="links">
    <li><span class="mark mark--blog"></span>sunnypathsandjoy.blogsite.example</li>
    <li><span class="mark mark--social"></span>SunnyPathsAndJoy</li>
  </ul>
</section>

</body>
</html>
```